Business Card Design Project

I need a business card designed that is clean, simple and elegant.
I am a fashion and advertising photographer based in Cape Town and Durban South Africa.
check out my website: www.marlowvance.co.za for ideas
Updates
Hi all,
Thanks for your submissions so far!
Please note:
I want no more than than black, white and/or grey to be used.
I don't want any photos used.
I would like the card to be double sided.
I would like to continue the design similar to the past ones Ive used.
I hope this helps, please send me further questions should you have any.
many thanks!
Marlow
Hi,
Please have a look at the jpg I loaded(called inspiration) which is the direction or inspiration I am aiming at.
Also PLEASE remember NO PHOTOS to be included on the card
many thanks!!
Target Market(s)
You can look at my site to get a better understanding of the audience:
www.marlowvance.co.za
Industry/Entity Type
Advertising
Requirements
Must have
- Clean design which can also be used for a watermark on photographs
perhaps black background with white text/grey
company called: Marlow Vance Photography
Nice to have
- below I have added logos that I have used in the past.
Should not have
- pictures of cameras
tacky elements

```html
<!DOCTYPE html>
<html lang="en">
<head>
<meta charset="utf-8">
<title>Marlow Vance Photography — Stationery</title>
<link rel="stylesheet" href="https://fonts.googleapis.com/css2?family=Inter:wght@300;400;700&display=swap">
<style>
  :root {
    --board: #7a4632;
    --ink: #000000;
    --paper: #ffffff;
    --grey-mid: #8a8a8a;
    --grey-soft: #c4c4c4;
    --grey-sheet: #9a9a9a;
    --grey-faint: #f1f1f1;
    --accent-red: #e0161b;
    --label: #f2ece8;
  }
  * { margin: 0; padding: 0; box-sizing: border-box; }
  html, body { width: 1200px; height: 840px; overflow: hidden; }
  body {
    background: var(--board);
    font-family: "Inter", Helvetica, Arial, sans-serif;
    position: relative;
  }
  .card {
    position: absolute;
    left: 59px;
    width: 454px;
    height: 260px;
    background: var(--ink);
    border-radius: 22px;
    box-shadow: 4px 6px 10px rgba(0,0,0,0.35);
    color: var(--paper);
  }
  .card--front { top: 40px; }
  .card--back { top: 336px; }
  .card-name {
    position: absolute;
    left: 50%; top: 50%;
    transform: translate(-50%, -50%);
    font-size: 38px;
    font-weight: 300;
    letter-spacing: 1px;
    white-space: nowrap;
  }
  .card-divider {
    position: absolute;
    left: 225px; top: 18px;
    width: 5px; height: 226px;
    background: var(--paper);
  }
  .studio {
    position: absolute;
    left: 12px; top: 106px;
    width: 206px;
  }
  .studio-name {
    font-size: 24px;
    line-height: 26px;
    font-weight: 300;
    letter-spacing: 0;
    white-space: nowrap;
  }
  .studio-name strong { font-weight: 700; }
  .studio-type {
    font-size: 23px;
    line-height: 26px;
    font-weight: 300;
    color: var(--grey-mid);
    letter-spacing: 1.6px;
  }
  .contact {
    position: absolute;
    right: 12px;
    text-align: right;
    white-space: nowrap;
  }
  .contact--email { top: 120px; font-size: 11px; font-weight: 300; color: var(--accent-red); }
  .contact--phone { font-size: 12.6px; font-weight: 300; }
  .contact--mobile { top: 164px; }
  .contact--office { top: 195px; }
  .contact--web { top: 229px; font-size: 16.5px; font-weight: 400; letter-spacing: -0.1px; }

  .caption {
    position: absolute;
    transform: translateX(-50%);
    font-size: 20px;
    font-weight: 300;
    color: var(--label);
    letter-spacing: 0.6px;
    white-space: nowrap;
  }
  .caption--card { left: 286px; top: 603px; }
  .caption--logo { left: 286px; top: 780px; }
  .caption--sheet { left: 897px; top: 780px; }

  .logo-set {
    position: absolute;
    left: 56px; top: 716px;
    width: 462px;
    display: flex;
    justify-content: space-between;
  }
  .logo-variant {
    width: 94px;
    font-size: 14.5px;
    font-weight: 400;
    text-align: center;
    white-space: nowrap;
  }
  .logo-variant--black { color: var(--ink); }
  .logo-variant--grey { color: var(--grey-mid); }
  .logo-variant--light { color: var(--grey-soft); }
  .logo-variant--red { color: var(--accent-red); }

  .letterhead {
    position: absolute;
    left: 646px; top: 40px;
    width: 501px; height: 708px;
    background: var(--grey-sheet);
    box-shadow: 4px 6px 12px rgba(0,0,0,0.35);
  }
  .letterhead-paper { position: absolute; inset: 0; }
  .letterhead-name {
    position: absolute;
    left: 56px; top: 74px;
    font-size: 15px;
    font-weight: 400;
    color: var(--ink);
    white-space: nowrap;
  }
  .letterhead-address {
    position: absolute;
    right: 50px; top: 74px;
    text-align: right;
    color: var(--ink);
  }
  .letterhead-address .title { font-size: 8.5px; line-height: 12px; font-weight: 400; }
  .letterhead-address .line { font-size: 5.4px; line-height: 8.4px; font-weight: 700; word-spacing: 3px; }
  .letterhead-mark {
    position: absolute;
    left: 250px; top: 560px;
    transform: translate(-50%, -50%);
    font-size: 42px;
    font-weight: 300;
    color: var(--grey-faint);
    white-space: nowrap;
  }
  .letterhead-web {
    position: absolute;
    left: 250px; top: 652px;
    transform: translateX(-50%);
    font-size: 15px;
    font-weight: 400;
    color: var(--ink);
    white-space: nowrap;
  }
</style>
</head>
<body>
  <section class="card card--front">
    <p class="card-name">Marlow Vance</p>
  </section>

  <section class="card card--back">
    <div class="studio">
      <p class="studio-name">MARLOW<strong>VANCE</strong></p>
      <p class="studio-type">PHOTOGRAPHY</p>
    </div>
    <div class="card-divider"></div>
    <p class="contact contact--email">marlow@marlowvance.co.za</p>
    <p class="contact contact--phone contact--mobile">+27 (0)82 555 0147</p>
    <p class="contact contact--phone contact--office">+27 (0)31 555 0192</p>
    <p class="contact contact--web">www.marlowvance.co.za</p>
  </section>
  <p class="caption caption--card">business card</p>

  <div class="logo-set">
    <span class="logo-variant logo-variant--black">Marlow Vance</span>
    <span class="logo-variant logo-variant--grey">Marlow Vance</span>
    <span class="logo-variant logo-variant--light">Marlow Vance</span>
    <span class="logo-variant logo-variant--red">Marlow Vance</span>
  </div>
  <p class="caption caption--logo">logo/watermark</p>

  <section class="letterhead">
    <svg class="letterhead-paper" width="501" height="708" viewBox="0 0 501 708" aria-hidden="true">
      <path d="M24,90 Q24,36 78,30 Q250,12 423,30 Q477,36 477,90 L477,620 Q477,672 423,678 Q250,696 78,678 Q24,672 24,620 Z" fill="#ffffff"/>
    </svg>
    <p class="letterhead-name">Marlow Vance</p>
    <div class="letterhead-address">
      <p class="title">Sample Text</p>
      <p class="line">sample text sample text sample text</p>
      <p class="line">sample text sample text sample text</p>
      <p class="line">sample text sample text sample text</p>
    </div>
    <p class="letterhead-mark">Marlow Vance</p>
    <p class="letterhead-web">www.marlowvance.co.za</p>
  </section>
  <p class="caption caption--sheet">letterhead</p>
</body>
</html>
```